Redesign of www.tidewellgallerynews.example.

I need to take the elements of a PixelHive website that was started some time ago but never went live with a website that I now have that is not very compelling. I publish a digital magazine through pagereel.example and link the magazine to www.tidewellgallerynews.example. Boring website.

The PixelHive website is: www.coveharborfunandshows.example. A lively website which is now too narrow in scope. I seek to expand my coverage to include the cultural life of my county.

Here's what I'd like to do.
1. Rename the PixelHive website using my url: www.tidewellgallerynews.example.
2. Use my tidewellgallerynews logo, replacing coveharborfunandshows.example
3. Break up the large rotating banner on the top into two spaces??? I want to feature my current magazine as the first placement. The space is too wide? Suggestions here appreciated. I also want back issues to be available for viewing.
4. I need flexibility to change headings, etc, so instruction needs to come with the design.
5. I'm thinking of offering blog space to others.

General question. Rather than moving everything over to www.coveharborfunandshows.example, should we just redesign www.tidewellgallerynews.example using the elements on the www.coveharborfunandshows.example site? Might be an easier way to go.

I'm open to a complete redesign of www.tidewellgallerynews.example with the exception of the logo and the spotlight on the magazines,both current and past issues.

I am in the middle of producing the next issue, so the website needs to not change until mid October. I'd like the design to be complete beforehand so we can make the change pretty quickly after the 15th of October.

I've attached covers of our last 2 issues and my logo. I'm open to a change in color with the logo,but not the fonts.

I'm not sure how many pages I'll need and I don't know the difference between coded and uncoded pages...so you can explain to me.

Target Market(s)

Readers who are interested in the arts and culture of the San Francisco Bay Area.

Number of Pages Required

4 page

Font styles to use
Other font styles liked:
• Whatever font is used at www.coveharborfunandshows.example

Colors

Designer to choose colors to be used in the design.

Requirements
Must have
• Current logo. Color suggestion for the website is fine.Featured space for the magazines. They are placed by my linking them from Pagereel.example over to my current website. www.coveharborfunandshows should be used as a template.
• WordPress for blogging and instructions included.
Nice to have
• Nice, bright, fun

```html
<!DOCTYPE html>
<html lang="en">
<head>
<meta charset="utf-8">
<title>Tidewell Gallery News — Contributors</title>
<link href="https://fonts.googleapis.com/css2?family=Noto+Sans:wght@300;400;700&family=Roboto+Condensed:wght@400;700&display=swap" rel="stylesheet">
<style>
  :root{
    --page:#ffffff;
    --orange-top:#c8340a;
    --orange-mid:#f2560b;
    --orange:#ff7408;
    --orange-accent:#f36a10;
    --tab:#f08a62;
    --card:#e6e6e6;
    --ink:#1a1a1a;
    --dark:#1c1c1c;
    --muted:#9a9a9a;
    --caption-bar:#7f7f7f;
    --footer-link:#fff1c9;
    --footer-copy:#ffb07a;
  }
  *{box-sizing:border-box;margin:0;padding:0}
  html,body{width:1200px;height:1200px;overflow:hidden;background:var(--page)}
  body{position:relative;font-family:"Noto Sans",Verdana,sans-serif;color:var(--ink)}
  .frame{position:absolute;left:139px;top:63px;width:922px;height:1011px;
    background:linear-gradient(180deg,var(--orange-top) 0%,var(--orange-mid) 22%,var(--orange) 45%,var(--orange) 100%)}
  .logo{position:absolute;left:231px;top:88px;color:#fff;font-weight:300;font-size:17px;line-height:22px;white-space:nowrap;display:flex;align-items:center;gap:6px}
  .logo-dot{width:7px;height:7px;background:#fff;border-radius:50%}
  .nav{position:absolute;left:424px;top:63px;height:72px;display:flex;align-items:center;font-size:8.8px;color:#fff;text-transform:uppercase;white-space:nowrap}
  .nav a{color:#fff;text-decoration:none;height:72px;display:flex;align-items:center;padding:0 11px}
  .nav .sep{opacity:.8}
  .nav a.active{background:var(--tab)}
  .panel{position:absolute;left:231px;top:136px;width:738px;height:882px;background:linear-gradient(180deg,#e9e9e9 0,#ffffff 60px,#ffffff 100%);box-shadow:0 1px 3px rgba(0,0,0,.25)}
  .hero{position:absolute;left:0;top:0;width:738px;height:251px;background:#111;overflow:hidden}
  .hero-photo{position:absolute;left:0;top:0;width:738px;height:251px;
    background:linear-gradient(90deg,#d8d8d8 0%,#9a9a9a 25%,#6a6a6a 45%,#2a2a2a 62%,#0d0d0d 78%,#000 100%)}
  .hero-badge{position:absolute;left:443px;top:61px;width:295px;height:26px;background:#fff;font-family:"Roboto Condensed",sans-serif;font-weight:700;font-size:15px;line-height:26px;padding-left:10px;color:#111}
  .hero-head{position:absolute;left:445px;top:102px;font-family:"Roboto Condensed",sans-serif;font-size:24px;line-height:23px;color:#a9a9a9;text-transform:uppercase;letter-spacing:-.3px}
  .hero-head b{font-weight:700}
  .arrow{position:absolute;top:106px;width:26px;height:26px;background:#cfcfcf;display:flex;align-items:center;justify-content:center}
  .arrow.prev{left:0;opacity:.6}
  .arrow.next{right:0}
  .dots{position:absolute;left:315px;top:225px;display:flex;gap:5px}
  .dots span{width:11px;height:11px;background:#666}
  .dots span.on{background:#fff}
  .section-head{position:absolute;left:28px;top:263px;width:680px;height:28px;border-bottom:1px solid #999}
  .section-head::after{content:"";position:absolute;left:0;bottom:-2px;width:95px;height:2px;background:var(--orange-accent)}
  .section-icon{position:absolute;left:0;top:0;width:26px;height:26px;background:var(--orange-accent);display:flex;align-items:center;justify-content:center}
  .section-title{position:absolute;left:34px;top:9px;font-size:11px;color:#222}
  .info{position:absolute;left:28px;top:300px;font-size:8.4px;color:#222}
  .info b{font-weight:700}
  .pager{position:absolute;right:30px;display:flex;align-items:center;gap:4px;font-size:8.2px;color:var(--muted)}
  .pager .btn,.load-more .btn{width:14px;height:13px;background:#d6d6d6;display:flex;align-items:center;justify-content:center}
  .pager .num{width:14px;height:13px;background:#b4b4b4;color:#fff;display:flex;align-items:center;justify-content:center}
  .pager.top{top:299px}
  .pager.bottom{top:855px}
  .load-more{position:absolute;left:28px;top:855px;display:flex;align-items:center;gap:5px;font-size:8.2px;color:var(--muted)}
  .card{position:absolute;width:331px;background:var(--card)}
  .card .photo-box{position:absolute;left:0;top:0;width:99px;height:100%;background:var(--dark)}
  .card .photo{position:absolute;left:13px;top:13px;width:74px;bottom:13px}
  .card .num{position:absolute;left:110px;top:0;width:22px;height:22px;background:var(--dark);color:#fff;font-size:8.5px;font-weight:700;display:flex;align-items:center;justify-content:center}
  .card .name{position:absolute;left:110px;right:11px;font-size:8.8px;font-weight:700;padding-bottom:2px;border-bottom:1px dotted #777}
  .card .bio{position:absolute;left:110px;right:11px;font-size:8.4px;line-height:10.4px;text-align:justify;color:#222}
  .footer-copy{position:absolute;left:231px;top:1039px;font-size:8.6px;color:var(--footer-copy)}
  .footer-nav{position:absolute;right:231px;top:1039px;font-size:8.6px;color:var(--footer-link);display:flex;gap:6px}
  .caption-bar{position:absolute;left:0;top:1098px;width:1200px;height:39px;background:var(--caption-bar);color:#fff;font-size:11.5px;font-weight:300;display:flex;align-items:center;justify-content:center}
</style>
</head>
<body>
  <div class="frame"></div>

  <div class="logo"><span>tidewell gallery news</span><span class="logo-dot"></span></div>

  <nav class="nav">
    <a href="#">Home</a><span class="sep">|</span>
    <a href="#">What we do</a><span class="sep">|</span>
    <a href="#" class="active">Contributors</a><span class="sep">|</span>
    <a href="#">Advertising</a><span class="sep">|</span>
    <a href="#">Subscribe Free!</a><span class="sep">|</span>
    <a href="#">Arts News</a><span class="sep">|</span>
    <a href="#">Contact</a>
  </nav>

  <main class="panel">
    <section class="hero">
      <div class="hero-photo" role="img" aria-label="Black and white photo of a printmaker smiling while working at a letterpress"></div>
      <div class="hero-badge">PREMIERE ISSUE</div>
      <div class="hero-head"><b>Written</b> for<br><b>Mariners</b> and<br><b>Love</b> the <b>arts</b><br><b>Their friends who</b></div>
      <div class="arrow prev"><svg width="10" height="12" viewBox="0 0 10 12"><path d="M8 1 L2 6 L8 11" fill="none" stroke="#fff" stroke-width="2.5"/></svg></div>
      <div class="arrow next"><svg width="10" height="12" viewBox="0 0 10 12"><path d="M2 1 L8 6 L2 11" fill="none" stroke="#222" stroke-width="2.5"/></svg></div>
      <div class="dots"><span class="on"></span><span></span><span></span><span></span><span></span><span></span><span></span></div>
    </section>

    <div class="section-head">
      <div class="section-icon"><svg width="10" height="14" viewBox="0 0 10 14"><path d="M2 1 L8 7 L2 13" fill="none" stroke="#fff" stroke-width="2.5"/></svg></div>
      <div class="section-title">CONTRIBUTORS</div>
    </div>
    <p class="info">For information on submissions, please email &nbsp;<b>editorial@tidewellgallerynews.example</b></p>
    <div class="pager top"><span class="btn"><svg width="6" height="8" viewBox="0 0 6 8"><path d="M1 1 L5 4 L1 7" fill="none" stroke="#fff" stroke-width="1.5"/></svg></span>Next<span class="num">2</span></div>

    <article class="card" style="left:28px;top:319px;height:114px">
      <div class="photo-box"><div class="photo" role="img" aria-label="Portrait of contributor Owen Halloway" style="background:linear-gradient(160deg,#d9d2c4,#8c7f6e)"></div></div>
      <div class="num">01</div>
      <h3 class="name" style="top:41px">Owen Halloway</h3>
      <p class="bio" style="top:57px">Owen Halloway has published several books on history, law, and of poetry. His poetry and legal, literary and historical essays have been widely published in literary and scholarly journals.</p>
    </article>

    <article class="card" style="left:378px;top:319px;height:114px">
      <div class="photo-box"><div class="photo" role="img" aria-label="Portrait of contributor Greta Lindqvist" style="background:linear-gradient(160deg,#d9b49a,#6b3b2c)"></div></div>
      <div class="num">02</div>
      <h3 class="name" style="top:36px">Greta Lindqvist</h3>
      <p class="bio" style="top:52px">Greta Lindqvist, owner of Sorrel Table in Healdsburg and Tiburon a food and wine pairing service working with wineries to create menus supporting wine sales at private and public events. Greta can be contacted at sorreltable@mailbox.example</p>
    </article>

    <article class="card" style="left:28px;top:447px;height:125px">
      <div class="photo-box"><div class="photo" role="img" aria-label="Black and white portrait of contributor Marisa Delvecchio Strand" style="background:linear-gradient(160deg,#e4e4e4,#8a8a8a)"></div></div>
      <div class="num">03</div>
      <h3 class="name" style="top:41px">Marisa Delvecchio Strand</h3>
      <p class="bio" style="top:57px">Marisa Delvecchio Strand focuses her career on supporting projects that build community and increase opportunities for the arts and those in need to have access to enriching and impactful experiences. She is currently Director of Development for Cove Street Playhouse.</p>
    </article>

    <article class="card" style="left:378px;top:447px;height:125px">
      <div class="photo-box"><div class="photo" role="img" aria-label="Portrait of contributor Desmond Archer in formal wear" style="background:linear-gradient(160deg,#7a4a36,#1e120e)"></div></div>
      <div class="num">04</div>
      <h3 class="name" style="top:28px">Desmond Archer</h3>
      <p class="bio" style="top:44px">Desmond Archer is a former weekly syndicated columnist for the Bayside Ledger and a winner of the prestigious Harlan Reed Award for excellence in journalism. He has been published in the Eastport Herald and Golden Gate Monthly. He currently writes a monthly column for the County Courier and is the Founder of The Songbook Circle.</p>
    </article>

    <article class="card" style="left:28px;top:586px;height:114px">
      <div class="photo-box"><div class="photo" role="img" aria-label="Portrait of contributor Peter Vance beside a red painting" style="background:linear-gradient(120deg,#d8362a 0%,#c9c4bc 55%,#2a2a2a 100%)"></div></div>
      <div class="num">05</div>
      <h3 class="name" style="top:41px">Peter Vance</h3>
      <p class="bio" style="top:57px">Peter Vance is a full-time artist who lives in the San Francisco Bay Area. His work can be found in both private and corporate collections worldwide.</p>
    </article>

    <article class="card" style="left:378px;top:586px;height:114px">
      <div class="photo-box"><div class="photo" role="img" aria-label="Outdoor portrait of contributor Russell Kemper" style="background:linear-gradient(160deg,#6f8a3a,#3b4a22)"></div></div>
      <div class="num">06</div>
      <h3 class="name" style="top:41px">Russell Kemper</h3>
      <p class="bio" style="top:57px">Russell Kemper is a full-time financial advisor and part-time photographer. Most of all, he's a loving husband and father, as expressed in his theme song submission.</p>
    </article>

    <article class="card" style="left:28px;top:714px;height:125px">
      <div class="photo-box"><div class="photo" role="img" aria-label="Portrait of contributor Nora Fitzgerald" style="background:linear-gradient(160deg,#d9c38a,#7a5a48)"></div></div>
      <div class="num">07</div>
      <h3 class="name" style="top:28px">Nora Fitzgerald</h3>
      <p class="bio" style="top:44px">Nora Fitzgerald is a Bay Area writer whose articles have appeared in the Bay City Dispatch, the Northshore Journal, the Coastline Weekly, the Bay Classical Notes and Bow &amp; Bridge Magazine. Passionate about music and the arts, she has performed as a folk, jazz and classical singer, and currently sings with the Tidewell Symphony Chorus.</p>
    </article>

    <article class="card" style="left:378px;top:714px;height:125px">
      <div class="photo-box"><div class="photo" role="img" aria-label="Black and white portrait of contributor Mateo Ferrand" style="background:linear-gradient(160deg,#5a5a5a,#0a0a0a)"></div></div>
      <div class="num">08</div>
      <h3 class="name" style="top:28px">Mateo Ferrand</h3>
      <p class="bio" style="top:44px">Mateo Ferrand is a media artist who works in responsive installations and interactive media design. He uses video, photography, installation, and mixed media to explore the complexity of human experiences such as immigration and identity. Mateo is the Communications &amp; Development Manager for Harbor Community Media Lab.</p>
    </article>

    <div class="load-more"><span class="btn"><svg width="8" height="6" viewBox="0 0 8 6"><path d="M1 1 L4 5 L7 1" fill="none" stroke="#fff" stroke-width="1.5"/></svg></span>Load More</div>
    <div class="pager bottom"><span class="btn"><svg width="6" height="8" viewBox="0 0 6 8"><path d="M1 1 L5 4 L1 7" fill="none" stroke="#fff" stroke-width="1.5"/></svg></span>Next<span class="num">2</span></div>
  </main>

  <p class="footer-copy">Copyright © 2017 Tidewell Gallery News &nbsp;|&nbsp; All rights reserved</p>
  <nav class="footer-nav">
    <span>Home</span><span>I</span><span>What We do</span><span>I</span><span>Contributors</span><span>I</span><span>Advertising</span><span>I</span><span>Subscribe Free!</span><span>I</span><span>Art News</span><span>I</span><span>Contact</span>
  </nav>

  <div class="caption-bar">WEB DESIGN &nbsp;: Contributors Page</div>
</body>
</html>
```